wolterhagen.info (Physiotherapeut)   //   quellbrand-athletic Webseite
wolterhagen.info (Physiotherapeut) // quellbrand-athletic Webseite
Zielgruppe
Die angesprochene Zielgruppe ist sportlich unterwegs (Sportler jeglicher Sportrichtung). Der externe Shop geht in Richtung Apparels / Kleidung.
Vielleicht wird es aber auch nur eine Physio-Seite und die Apparels kommen im zweiten Schritt - das liegt am Design das man mir präsentiert .... Also legt los ...
(KELVARO wird HOST)
Aufgabenstellung
Mein Name ist Jonathan Wolterhagen ich bin Physiotherapeut / Osteopath (etc).
Die Domain www.wolterhagen.info gehört mir und es würde auch für den Anfang reichen eine digitale Visitenkarte von mir zu erstellen ...
Weiter möchte ich eine Webseite mit dem Namen "quellbrand-athletic" eröffnen. [COM/DE]
Die zu kreierenden Seiten innerhalb der Domain quellbrand-athleti sind:
Main-/LandingPage,
ShopPage (Weiterleitung zu einer externen Webseite),
Impressum,
KooperationsPage (andere Projekte bzw. Webseiten von mir, die in Zukunft kommen).
Design-Vorschläge und umsetzbare / hochladbare Pages (KELVARO) oder NUR Grafiken sind gerne gesehen ...
Die angesprochene Zielgruppe ist sportlich unterwegs (Sportler jeglicher Sportrichtung). Der externe Shop geht in Richtung Apparels.
Die angesprochenen Kreaturen brauchen ein Heim, dass durch ein Schloss repräsentiert werden soll. Evtl. ein Labor. Nicht zu kindlich! Nicht zu düster oder blutig.
Was ich möchte ist: Corporate Identity, eine Webpage (host der Domain wird KELVARO), Logo, etc
Zweiter Schritt wird sein: Grafiken für die Apparels / Klamotten.

```html
<!DOCTYPE html>
<html lang="en">
<head>
<meta charset="utf-8">
<title>Wolterhagen Jonathan – Physical Therapist</title>
<link href="https://fonts.googleapis.com/css2?family=Source+Sans+3:wght@400;600;700&display=swap" rel="stylesheet">
<style>
:root{
  --green:#8cc63f;
  --green-dark:#0b5a0e;
  --green-line:#2f7d1c;
  --faint:#dcefd2;
  --white:#ffffff;
  --ink:#1a1a1a;
  --sky:#bfe3f2;
  --rock:#8a6a55;
}
*{margin:0;padding:0;box-sizing:border-box}
html,body{width:1053px;height:1200px;overflow:hidden}
body{font-family:"Source Sans 3",sans-serif;background:var(--green);color:var(--white);position:relative}
.topbar{position:absolute;left:0;top:0;width:1053px;height:18px;background:var(--green)}
.topbar__tagline{position:absolute;left:343px;top:4px;font-size:7px;letter-spacing:.2px;color:var(--white)}
.topbar__social{position:absolute;left:601px;top:3px;display:flex;gap:1px}
.dot{width:11px;height:11px;border-radius:50%;background:var(--white);display:block}
.lang{position:absolute;left:663px;top:2px;width:49px;height:13px;border:1px solid var(--white);display:flex;align-items:center;gap:4px;padding-left:3px;font-size:6px}
.lang__flag{width:12px;height:7px;background:#c9d3e6}
.header{position:absolute;left:0;top:18px;width:1053px;height:187px;background:var(--white);overflow:hidden}
.header__art{position:absolute;top:0;height:187px;width:300px}
.header__art--left{left:0;background:linear-gradient(90deg,var(--faint),rgba(255,255,255,0) 100%)}
.header__art--right{right:0;background:linear-gradient(270deg,var(--faint),rgba(255,255,255,0) 100%)}
.brand{position:absolute;left:0;width:1053px;top:33px;text-align:center}
.brand__mark{width:56px;height:56px;border-radius:50%;background:var(--green-dark);margin:0 auto}
.brand__name{margin-top:22px;font-size:15px;font-weight:600;color:var(--ink);letter-spacing:.2px}
.nav{position:absolute;left:337px;top:152px;width:380px;height:20px}
.nav a{position:absolute;top:0;font-size:11px;color:var(--green-line);text-decoration:none}
.nav a.is-active{font-weight:700;color:var(--green-dark)}
.nav__rule{position:absolute;left:0;top:19px;width:380px;height:1px;background:linear-gradient(90deg,rgba(47,125,28,0),var(--green-line) 15%,var(--green-line) 85%,rgba(47,125,28,0))}
.content{position:absolute;left:0;top:205px;width:1053px;height:510px}
.intro{position:absolute;left:160px;top:40px;width:367px;font-size:10.6px;line-height:14.3px;text-align:justify;hyphens:auto}
.intro__photo{float:left;width:176px;height:133px;margin:5px 8px 2px 0;background:linear-gradient(135deg,#d9d9d9,#9a9a9a 60%,#3d8fc4)}
.news{position:absolute;left:603px;top:43px;width:293px}
.news__item{margin-bottom:11px}
.news__title{font-size:10.8px;font-weight:700;margin-bottom:2px}
.news__text{font-size:6.7px;line-height:9.5px;text-align:justify}
.hero{position:absolute;left:0;top:715px;width:1053px;height:331px;background:linear-gradient(180deg,var(--sky) 0%,#b89b86 40%,var(--rock) 70%,#4a3a30 100%)}
.footer__rule{position:absolute;left:237px;top:1095px;width:585px;height:1px;background:linear-gradient(90deg,rgba(11,90,14,0),var(--green-dark) 20%,var(--green-dark) 80%,rgba(11,90,14,0))}
.footer__nav{position:absolute;left:292px;top:1116px;display:flex;flex-direction:column;gap:4px;font-size:7px;line-height:10px}
.footer__nav a{color:var(--white);text-decoration:none}
.footer__legal{position:absolute;left:380px;top:1116px;width:293px;font-size:5.1px;line-height:7px;text-align:justify}
.footer__contact{position:absolute;left:689px;top:1116px;font-size:7px;line-height:9.5px}
.footer__contact a{color:#1a3cc7;text-decoration:underline}
.follow{display:flex;align-items:center;gap:6px;margin-top:4px;font-size:5.5px}
.follow__icons{display:flex;gap:1px}
</style>
</head>
<body>
<div class="topbar">
  <span class="topbar__tagline">PHYSICAL THERAPIST · OSTEOPATHIC MEDICINE</span>
  <div class="topbar__social" aria-label="Social networks"><span class="dot"></span><span class="dot"></span><span class="dot"></span><span class="dot"></span></div>
  <div class="lang"><span class="lang__flag"></span>English</div>
</div>

<header class="header">
  <div class="header__art header__art--left" role="img" aria-label="Faint anatomical illustration of athletes in motion"></div>
  <div class="header__art header__art--right" role="img" aria-label="Faint anatomical illustration of a flexing figure"></div>
  <div class="brand">
    <div class="brand__mark"></div>
    <div class="brand__name">Wolterhagen Jonathan</div>
  </div>
  <nav class="nav">
    <a class="is-active" href="#" style="left:4px">Main</a>
    <a href="#" style="left:82px">News</a>
    <a href="#" style="left:158px">Shop</a>
    <a href="#" style="left:228px">Contacts</a>
    <a href="#" style="left:310px">Cooperation</a>
    <span class="nav__rule"></span>
  </nav>
</header>

<main class="content">
  <div class="intro">
    <div class="intro__photo" role="img" aria-label="Portrait photo of the therapist"></div>
    Lorem ipsum dolor sit amet, consectetur adipiscing elit, sed do eiusmod tempor incididunt ut labore et dolore magna aliqua. Ut enim ad minim veniam, quis nostrud exercitation ullamco laboris nisi ut aliquip ex ea commodo consequat. Duis aute irure dolor in reprehenderit in voluptate velit esse cillum dolore eu fugiat nulla pariatur. Excepteur sint occaecat cupidatat non proident, sunt in culpa qui officia deserunt mollit anim id est laborum.<br>
    Lorem ipsum dolor sit amet, consectetur adipiscing elit, sed do eiusmod tempor incididunt ut labore et dolore magna aliqua. Ut enim ad minim veniam, quis nostrud exercitation ullamco laboris nisi ut aliquip ex ea commodo consequat. Duis aute irure dolor in reprehenderit in voluptate velit esse cillum dolore eu fugiat nulla pariatur. Excepteur sint occaecat cupidatat non proident, sunt in culpa qui officia deserunt mollit anim id est laborum. Lorem ipsum dolor sit amet, consectetur adipiscing elit, sed do eiusmod tempor incididunt ut labore et dolore magna aliqua. Ut enim ad minim veniam, quis nostrud exercitation ullamco laboris nisi ut aliquip ex ea commodo consequat. Duis aute irure dolor in reprehenderit in voluptate velit esse cillum dolore eu fugiat nulla pariatur. Excepteur sint occaecat cupidatat non proident, sunt in culpa qui officia deserunt mollit anim id est laborum.Lorem ipsum dolor sit amet, consectetur adipiscing elit, sed do eiusmod tempor incididunt ut labore et dolore magna aliqua. Ut enim ad minim veniam, quis nostrud exercitation ullamco laboris nisi ut aliquip ex ea commodo consequat. Duis aute irure dolor in reprehenderit in voluptate velit esse cillum dolore eu fugiat nulla pariatur. Excepteur sint occaecat cupidatat non proident, sunt in culpa qui officia deserunt mollit anim id est
  </div>

  <section class="news">
    <article class="news__item">
      <h2 class="news__title">Latest News</h2>
      <p class="news__text">Lorem ipsum dolor sit amet, consectetur adipiscing elit, sed do eiusmod tempor incididunt ut labore et dolore magna aliqua. Ut enim ad minim veniam, quis nostrud exercitation ullamco laboris nisi ut aliquip ex ea commodo consequat. Duis aute irure dolor in reprehenderit in voluptate velit esse cillum dolore eu fugiat nulla pariatur. Excepteur sint occaecat cupidatat non proident, sunt in culpa qui officia deserunt mollit anim id est laborum.</p>
    </article>
    <article class="news__item">
      <h2 class="news__title">Latest News</h2>
      <p class="news__text">Lorem ipsum dolor sit amet, consectetur adipiscing elit, sed do eiusmod tempor incididunt ut labore et dolore magna aliqua. Ut enim ad minim veniam, quis nostrud exercitation ullamco laboris nisi ut aliquip ex ea commodo consequat. Duis aute irure dolor in reprehenderit in voluptate velit esse cillum dolore eu fugiat nulla pariatur. Excepteur sint occaecat cupidatat non proident, sunt in culpa qui officia deserunt mollit anim id est laborum. Lorem ipsum dolor sit amet, consectetur adipiscing elit, sed do eiusmod tempor incididunt ut labore et dolore magna aliqua. Ut enim ad minim veniam, quis nostrud exercitation ullamco laboris nisi ut aliquip ex ea commodo consequat. Duis aute irure dolor in reprehenderit in voluptate velit esse cillum dolore eu fugiat nulla pariatur. Excepteur sint</p>
    </article>
    <article class="news__item">
      <h2 class="news__title">Latest News</h2>
      <p class="news__text">Lorem ipsum dolor sit amet, consectetur adipiscing elit, sed do eiusmod tempor incididunt ut labore et dolore magna aliqua. Ut enim ad minim veniam, quis nostrud exercitation ullamco laboris nisi ut aliquip ex ea commodo consequat. Duis aute irure dolor in reprehenderit in voluptate velit esse cillum dolore eu fugiat nulla pariatur. Excepteur sint occaecat cupidatat non proident, sunt in culpa qui officia deserunt mollit anim id est laborum. Lorem ipsum dolor sit amet, consectetur adipiscing elit, sed do eiusmod tempor incididunt ut labore et dolore magna aliqua. Ut enim ad minim veniam, quis nostrud exercitation ullamco laboris nisi ut aliquip ex ea commodo consequat. Duis aute irure dolor in reprehenderit in voluptate velit esse cillum dolore eu fugiat nulla pariatur. Excepteur sint</p>
    </article>
    <article class="news__item">
      <h2 class="news__title">Latest News</h2>
      <p class="news__text">Lorem ipsum dolor sit amet, consectetur adipiscing elit, sed do eiusmod tempor incididunt ut labore et dolore magna aliqua. Ut enim ad minim veniam, quis nostrud exercitation ullamco laboris nisi ut aliquip ex ea commodo consequat. Duis aute irure dolor in reprehenderit in voluptate velit esse cillum dolore eu fugiat nulla pariatur. Excepteur sint occaecat cupidatat non proident, sunt in culpa qui officia deserunt mollit anim id est laborum. Lorem ipsum dolor sit amet, consectetur adipiscing elit, sed do eiusmod tempor incididunt ut labore et dolore magna aliqua. Ut enim ad minim veniam, quis nostrud exercitation ullamco laboris nisi ut aliquip ex ea commodo consequat. Duis aute irure dolor in reprehenderit in voluptate velit esse cillum dolore eu fugiat nulla pariatur. Excepteur sint</p>
    </article>
  </section>
</main>

<div class="hero" role="img" aria-label="Photo of a runner sprinting in front of mountain cliffs under a blue sky"></div>

<footer>
  <span class="footer__rule"></span>
  <nav class="footer__nav">
    <a href="#">Main</a><a href="#">News</a><a href="#">Shop</a><a href="#">Contacts</a><a href="#">Cooperation</a>
  </nav>
  <p class="footer__legal">Copyright information. Copyright information. Copyright information. Copyright information. Copyright information. Copyright information. Copyright information. Copyright information. Copyright information. Copyright information. Copyright information. Copyright information. Copyright information. Copyright information. Copyright information. Copyright information. Copyright information. Copyright information. Copyright information. Copyright information. Copyright information. Copyright information. Copyright information. Copyright information. Copyright information. Copyright information. Copyright information. Copyright information. Copyright information. Copyright information. Copyright information. Copyright information. Copyright information. Copyright information. Copyright information. Copyright information. Copyright information. Copyright information. Copyright information. Copyright information. Copyright information. Copyright information. Copyright information. Copyright information. Copyright information.</p>
  <address class="footer__contact" style="font-style:normal">
    Contact Us<br>Lindenweg 14<br>26135 Feldhausen<br>Tel: +49 (0)4405 555-190<br>E-mail: <a href="#">info@wolterhagen.info</a>
    <div class="follow">Follow Us <span class="follow__icons"><span class="dot"></span><span class="dot"></span><span class="dot"></span><span class="dot"></span></span></div>
  </address>
</footer>
</body>
</html>
```